Product Menu 8 x 11- Home Inspection Company Ancillary Services

Hello, on the front side of the flyer will be all about sewer camera inspections. These will include the images of the damages on the front and the information on the Sewer Scope Inspections: Safeguard Your Home from Hidden Plumbing Issues.
On the back will include indoor air quality. Solar Panel Inspections, Roof Certifications, and Expert Raised Foundation Review.
Please use logo and colors as a branding guide for the flyer.
$275- Sewer Camera Fee
$495 -Indoor Air Quality Inspection- Getting an indoor air quality (IAQ) inspection for mold when buying a home is crucial for health, safety, and financial protection. Mold can cause serious respiratory issues, especially for those with allergies or asthma, and toxic molds like black mold pose additional risks. It often grows in hidden areas, such as behind walls or in HVAC systems, often linked to water damage or structural issues. Early detection allows you to negotiate remediation costs, prevent mold from spreading, and avoid expensive repairs, ensuring a safe and sound investment.
$395 -Solar Panel Inspection- Getting a solar panel inspection when buying a home is essential to ensure efficiency, safety, and long-term savings. It verifies the system’s condition, identifying issues like damaged panels, faulty wiring, or inefficient inverters that could impact performance or pose safety risks. The inspection also evaluates the system’s energy output and compatibility with your energy needs, ensuring you’re benefiting from the investment. Additionally, understanding the age, warranty, and maintenance history of the system helps avoid unexpected repair costs and maximizes the value of this eco-friendly feature.
$399 Roof Certifications- Obtaining a roof certification when buying a home is vital for assessing the roof's condition, lifespan, and potential repair needs. This certification provides a professional evaluation, ensuring the roof is free from leaks, damage, or structural issues, which could lead to costly repairs. Many insurance companies require a roof certification before issuing or renewing a policy, particularly for older roofs, to confirm it meets safety standards. Having this certification not only provides peace of mind but also helps facilitate insurance coverage and protects your investment in the property.
$199- Advanced Foundation Review-An advanced foundation review by a licensed foundation contractor is essential when buying a home, as it provides a detailed assessment beyond what a general home inspector can offer. While home inspectors are trained generalists who identify visible issues, a foundation contractor is a specialist with the expertise to evaluate structural integrity, detect hidden problems, and determine the severity of any concerns. This specialized review can uncover issues like uneven settling, cracks, or drainage problems that may require repairs, ensuring you have a clear understanding of the foundation's condition before making a significant investment.
Real Estate Buyers and Real Estate Agents

```html
<!DOCTYPE html>
<html lang="en">
<head>
<meta charset="utf-8">
<title>Summit Crest – Sewer Scope & Ancillary Services</title>
<link href="https://fonts.googleapis.com/css2?family=Montserrat:wght@500;600;700;800&family=Poppins:wght@600;700&display=swap" rel="stylesheet">
<style>
:root{
  --blue:#0a5aa8;
  --blue-dark:#0b3f7d;
  --red:#e21d27;
  --ink:#1b1b1b;
  --stage:#b7b5b6;
  --white:#ffffff;
  --line:#c9ccd3;
}
*{margin:0;padding:0;box-sizing:border-box}
html,body{width:1200px;height:1200px;overflow:hidden;background:var(--stage);font-family:"Montserrat",sans-serif;color:var(--ink)}
.sheet{position:absolute;top:278px;width:535px;height:734px;background:var(--white);overflow:hidden;box-shadow:0 4px 12px rgba(0,0,0,.18)}
.sheet--front{left:45px}
.sheet--back{left:613px}
.abs{position:absolute}
.bg{position:absolute;inset:0}
.brand{position:absolute;display:flex;flex-direction:column;align-items:center;gap:5px}
.brand__dot{width:52px;height:52px;border-radius:50%;background:var(--blue)}
.brand__name{font-family:"Poppins",sans-serif;font-weight:700;font-size:12px;color:var(--blue);letter-spacing:.5px;white-space:nowrap}
.hero-photo{position:absolute;left:240px;top:63px;width:260px;height:202px;clip-path:polygon(14% 0,100% 0,100% 100%,14% 100%,0 50%);background:radial-gradient(ellipse at 55% 25%,#1f1a14 0 12%,#6b5338 30%,#5a4a3a 60%,#8a7f6a 100%);border-radius:10px}
.title{position:absolute;left:42px;font-family:"Montserrat",sans-serif;font-weight:800;line-height:1}
.title--sewer{top:122px;font-size:38px;color:var(--red);letter-spacing:-.5px}
.title--scope{top:157px;font-size:38px;color:var(--white);letter-spacing:-.5px}
.title--insp{top:193px;font-size:25px;color:var(--white)}
.tagline{position:absolute;left:44px;top:236px;padding-left:12px;border-left:2px solid var(--white);font-family:"Poppins",sans-serif;font-weight:700;font-size:14.5px;line-height:17px;color:var(--white)}
.h-what{position:absolute;left:42px;top:314px;font-weight:800;font-size:12.5px;line-height:14px}
.h-what .hl,.card__title .hl,.reason__title{color:var(--blue)}
.body{font-size:7.5px;line-height:9px;font-weight:500;color:var(--ink)}
.what-text{position:absolute;left:42px;top:355px;width:162px;font-size:7.3px}
.thumb{position:absolute;top:339px;width:92px;height:76px;background:var(--white);box-shadow:0 2px 5px rgba(0,0,0,.3);padding:3px}
.thumb__img{width:100%;height:52px;background:radial-gradient(circle at 50% 45%,#1c2430 0 10%,#4b5f78 35%,#6e6a66 100%)}
.thumb__cap{font-size:4.6px;line-height:5.4px;font-weight:700;text-align:center;margin-top:2px}
.why{position:absolute;left:42px;top:432px;width:451px;display:flex;align-items:center;gap:8px;font-weight:800;font-size:12px;white-space:nowrap}
.why::before,.why::after{content:"";flex:1;height:1px;background:#444}
.why .hl{color:var(--blue)}
.reason{position:absolute;width:205px}
.reason__head{display:flex;align-items:center;gap:6px;height:18px}
.reason__icon{width:16px;height:16px;border-radius:50%;background:var(--red);flex:none;display:flex;align-items:center;justify-content:center}
.reason__title{font-family:"Poppins",sans-serif;font-weight:700;font-size:9px}
.reason .body{margin-top:4px}
.badge{position:absolute;top:616px;width:54px;height:54px;border-radius:50%;box-shadow:0 2px 4px rgba(0,0,0,.35)}
.badge--red{left:290px;background:radial-gradient(circle,#fff 0 45%,var(--red) 47%)}
.badge--gold{left:361px;background:radial-gradient(circle,#e7c35a 0 55%,#b8902a 57%,#f2d77a 80%)}
.badge--gray{left:432px;background:radial-gradient(circle,#d6d2c4 0 50%,#55534d 52%)}
.footer{position:absolute;left:0;top:680px;width:535px;height:54px}
.footer__phone{position:absolute;left:44px;top:14px;display:flex;align-items:center;gap:6px;color:var(--white);font-weight:700;font-size:10.5px}
.footer__contacts{position:absolute;left:176px;top:15px;display:flex;gap:12px;font-size:9.3px;font-weight:500;color:var(--ink)}
.footer__contacts span{display:flex;align-items:center;gap:4px}
.fee{position:absolute;left:33px;top:26px;display:flex;align-items:center;gap:7px}
.fee__price{font-family:"Montserrat",sans-serif;font-weight:800;font-size:44px;color:var(--red);letter-spacing:-1px;line-height:1}
.fee__price sup{font-size:20px;vertical-align:top;position:relative;top:2px}
.fee__label{font-family:"Poppins",sans-serif;font-weight:700;font-size:17px;line-height:19px;color:var(--white)}
.card{position:absolute;left:38px;width:458px;background:var(--white);border:1px solid var(--line);border-radius:8px;box-shadow:0 4px 8px rgba(0,0,0,.18)}
.card__tab{position:absolute;right:-1px;top:-1px;width:103px;height:30px;border-radius:0 8px 0 0;clip-path:polygon(0 0,100% 0,100% 100%,12% 100%);display:flex;align-items:center;justify-content:center;color:var(--white);font-family:"Montserrat",sans-serif;font-weight:800;font-size:20px}
.card__tab sup{font-size:10px;vertical-align:top;margin-right:1px}
.card__tab--red{background:var(--red)}
.card__tab--blue{background:var(--blue)}
.card__title{position:absolute;left:20px;top:15px;font-weight:800;font-size:12.5px;color:var(--ink)}
.card__text{position:absolute;left:20px;top:35px;width:300px;font-size:7.4px;line-height:8.9px}
.card__img{position:absolute;left:338px;width:106px;height:72px;border:2px solid var(--white);box-shadow:0 1px 4px rgba(0,0,0,.35)}
</style>
</head>
<body>

<section class="sheet sheet--front">
  <svg class="bg" width="535" height="734" viewBox="0 0 535 734" aria-hidden="true">
    <polygon points="265,0 535,0 535,110 200,110" fill="#e21d27"/>
    <polygon points="0,103 240,103 292,28 535,28 535,298 248,298 272,226 0,226" fill="#0a5aa8"/>
    <polygon points="0,226 285,226 248,293 0,293" fill="#e21d27"/>
  </svg>

  <div class="brand" style="left:70px;top:22px">
    <div class="brand__dot"></div>
    <div class="brand__name">SUMMIT CREST</div>
  </div>

  <div class="hero-photo" role="img" aria-label="Camera view inside a sewer pipe blocked by tree roots and standing water"></div>

  <h1 class="title title--sewer">SEWER</h1>
  <div class="title title--scope">SCOPE</div>
  <div class="title title--insp">INSPECTIONS</div>
  <p class="tagline">Safeguard Your Home<br>from Hidden Plumbing<br>Issues</p>

  <h2 class="h-what"><span class="hl">WHAT IS A SEWER</span><br>SCOPE INSPECTION?</h2>
  <p class="body what-text">A sewer scope inspection uses a camera to inspect your home's sewer lines. The camera is inserted into the sewer pipe, allowing an inspector to detect blockages, cracks, tree root intrusions, and other issues that can cause significant damage if left unaddressed.</p>

  <figure class="thumb" style="left:215px">
    <div class="thumb__img" role="img" aria-label="Sewer camera still showing root intrusion"></div>
    <figcaption class="thumb__cap">Root intrusion present in Black ABS section of sewer line at 53 feet.</figcaption>
  </figure>
  <figure class="thumb" style="left:320px">
    <div class="thumb__img" role="img" aria-label="Sewer camera still showing debris and clog"></div>
    <figcaption class="thumb__cap">Debris and clog in sewer line at 71 feet.</figcaption>
  </figure>
  <figure class="thumb" style="left:414px">
    <div class="thumb__img" role="img" aria-label="Sewer camera still showing a clog"></div>
    <figcaption class="thumb__cap">Clog in sewer line at 72 feet.</figcaption>
  </figure>

  <h2 class="why"><span><span class="hl">WHY YOU SHOULD GET A</span> SEWER SCOPE INSPECTION</span></h2>

  <div class="reason" style="left:42px;top:459px">
    <div class="reason__head"><span class="reason__icon"><svg width="8" height="8" viewBox="0 0 8 8"><path d="M4 0.5 7 2v2.5C7 6 5.6 7.2 4 7.6 2.4 7.2 1 6 1 4.5V2z" fill="#fff"/></svg></span><h3 class="reason__title">Prevent Costly Repairs</h3></div>
    <p class="body">Sewer line issues can be extremely expensive to fix, with some repairs costing thousands of dollars. A sewer scope inspection can identify problems early, potentially saving you from dealing with costly repairs down the road.</p>
  </div>
  <div class="reason" style="left:287px;top:459px">
    <div class="reason__head"><span class="reason__icon"><svg width="8" height="8" viewBox="0 0 8 8"><path d="M3 1h2v2h2v2H5v2H3V5H1V3h2z" fill="#fff"/></svg></span><h3 class="reason__title">Avoid Health Hazards</h3></div>
    <p class="body">Faulty sewer systems can lead to sewage backups, which are not only unpleasant but also pose serious health risks. Inspections help ensure your home's plumbing is functioning safely.</p>
  </div>
  <div class="reason" style="left:42px;top:532px">
    <div class="reason__head"><span class="reason__icon"><svg width="8" height="8" viewBox="0 0 8 8"><path d="M4 1 7.5 4H6.5V7h-5V4H.5z" fill="#fff"/></svg></span><h3 class="reason__title">Protect Your Investment</h3></div>
    <p class="body">Whether you're buying or selling a home, understanding the condition of the sewer system can impact your decision. For buyers, it helps avoid unexpected expenses. For sellers, it can provide peace of mind and ensure the sale goes smoothly.</p>
  </div>
  <div class="reason" style="left:287px;top:533px">
    <div class="reason__head"><span class="reason__icon"><svg width="8" height="8" viewBox="0 0 8 8"><path d="M1.2 4.2 3.2 6.2 6.8 1.8" stroke="#fff" stroke-width="1.4" fill="none"/></svg></span><h3 class="reason__title">Ensure Proper Functioning</h3></div>
    <p class="body">A sewer scope inspection gives you a better understanding of how well your sewer system is functioning. It helps detect potential issues like blockages from tree roots, misaligned pipes, or wear and tear that may cause drainage problems.</p>
  </div>
  <div class="reason" style="left:42px;top:608px">
    <div class="reason__head"><span class="reason__icon"><svg width="8" height="8" viewBox="0 0 8 8"><ellipse cx="4" cy="4" rx="3.3" ry="2" stroke="#fff" stroke-width="1" fill="none"/><circle cx="4" cy="4" r="1" fill="#fff"/><path d="M1 7 7 1" stroke="#fff" stroke-width="1"/></svg></span><h3 class="reason__title">Catch Hidden Problems</h3></div>
    <p class="body">Sewer line issues often remain hidden until it's too late. Without a sewer scope inspection, it's nearly impossible to identify problems that could lead to sewage backups, unpleasant odors, and costly damages.</p>
  </div>

  <span class="badge badge--red" role="img" aria-label="Discount program badge"></span>
  <span class="badge badge--gold" role="img" aria-label="Master inspector certification badge"></span>
  <span class="badge badge--gray" role="img" aria-label="Professional inspector certification badge"></span>

  <footer class="footer">
    <svg class="bg" width="535" height="54" viewBox="0 0 535 54" aria-hidden="true">
      <polygon points="0,0 150,0 186,49 0,49" fill="#0a5aa8"/>
      <polygon points="157,0 163,0 199,46 193,46" fill="#e21d27"/>
      <rect x="186" y="45" width="349" height="3" fill="#e21d27"/>
      <rect x="0" y="49" width="535" height="5" fill="#0a5aa8"/>
    </svg>
    <div class="footer__phone"><svg width="9" height="9" viewBox="0 0 10 10"><path d="M2 .5 4 2.5 3 4c.6 1.3 1.7 2.4 3 3l1.5-1 2 2-1.5 1.5C4.5 9.5.5 5.5.5 2z" fill="#e21d27"/></svg>800-555-0142</div>
    <div class="footer__contacts">
      <span><svg width="10" height="7" viewBox="0 0 10 7"><rect width="10" height="7" fill="#e21d27"/><path d="M0 0 5 4 10 0" stroke="#fff" fill="none"/></svg>hello@summitcrestinspect.com</span>
      <span><svg width="9" height="9" viewBox="0 0 10 10"><circle cx="5" cy="5" r="4.3" stroke="#e21d27" fill="none"/><ellipse cx="5" cy="5" rx="2" ry="4.3" stroke="#e21d27" fill="none"/><path d="M.7 5h8.6" stroke="#e21d27"/></svg>www.summitcrestinspect.com</span>
    </div>
  </footer>
</section>

<section class="sheet sheet--back">
  <svg class="bg" width="535" height="100" viewBox="0 0 535 100" aria-hidden="true">
    <polygon points="0,0 275,0 240,94 0,94" fill="#0a5aa8"/>
    <rect x="0" y="94" width="535" height="4" fill="#0a5aa8"/>
  </svg>
  <div class="abs" role="img" aria-label="Inside view of a clean sewer pipe" style="left:252px;top:0;width:162px;height:94px;clip-path:polygon(23% 0,100% 0,100% 100%,0 100%);background:radial-gradient(ellipse at 40% 55%,#1a1815 0 14%,#6f6a63 35%,#b8b2a8 70%,#8d877d 100%)"></div>
  <div class="brand" style="left:418px;top:20px">
    <div class="brand__dot" style="width:44px;height:44px"></div>
    <div class="brand__name" style="font-size:10.5px">SUMMIT CREST</div>
  </div>

  <div class="fee">
    <span class="fee__price"><sup>$</sup>275</span>
    <span class="fee__label">Sewer<br>Camera Fee</span>
  </div>

  <article class="card" style="top:110px;height:121px">
    <div class="card__tab card__tab--red"><sup>$</sup>495</div>
    <h2 class="card__title"><span class="hl">INDOOR AIR</span> QUALITY INSPECTION</h2>
    <p class="body card__text">Getting an indoor air quality (IAQ) inspection for mold when buying a home is crucial for health, safety, and financial protection. Mold can cause serious respiratory issues, especially for those with allergies or asthma, and toxic molds like black mold pose additional risks. It often grows in hidden areas, such as behind walls or in HVAC systems, often linked to water damage or structural issues. Early detection allows you to negotiate remediation costs, prevent mold from spreading, and avoid expensive repairs, ensuring a safe and sound investment.</p>
    <div class="card__img" role="img" aria-label="Hand holding a moisture meter against a window frame" style="top:37px;background:linear-gradient(135deg,#f4f6f8,#dfe4ea 60%,#c9a38d)"></div>
  </article>

  <article class="card" style="top:250px;height:123px">
    <div class="card__tab card__tab--blue"><sup>$</sup>395</div>
    <h2 class="card__title"><span class="hl">SOLAR PANEL</span> INSPECTION</h2>
    <p class="body card__text" style="top:33px">Getting a solar panel inspection when buying a home is essential to ensure efficiency, safety, and long-term savings. It verifies the system's condition, identifying issues like damaged panels, faulty wiring, or inefficient inverters that could impact performance or pose safety risks. The inspection also evaluates the system's energy output and compatibility with your energy needs, ensuring you're benefiting from the investment. Additionally, understanding the age, warranty, and maintenance history of the system helps avoid unexpected repair costs and maximizes the value of this eco-friendly feature.</p>
    <div class="card__img" role="img" aria-label="House roof covered with solar panels" style="top:37px;background:linear-gradient(170deg,#dfe8f1 0 25%,#2f4f78 40%,#5a6f8a 60%,#c8b49a 80%,#8aa37a)"></div>
  </article>

  <article class="card" style="top:391px;height:121px">
    <div class="card__tab card__tab--red"><sup>$</sup>399</div>
    <h2 class="card__title"><span class="hl">ROOF</span> CERTIFICATIONS</h2>
    <p class="body card__text" style="width:308px">Obtaining a roof certification when buying a home is vital for assessing the roof's condition, lifespan, and potential repair needs. This certification provides a professional evaluation, ensuring the roof is free from leaks, damage, or structural issues, which could lead to costly repairs. Many insurance companies require a roof certification before issuing or renewing a policy, particularly for older roofs, to confirm it meets safety standards. Having this certification not only provides peace of mind but also helps facilitate insurance coverage and protects your investment in the property.</p>
    <div class="card__img" role="img" aria-label="Inspector working on a shingle roof" style="top:37px;background:linear-gradient(160deg,#7c9a5c 0 25%,#c9cdd2 45%,#1f2f4f 60%,#8e8a86)"></div>
  </article>

  <article class="card" style="top:531px;height:123px">
    <div class="card__tab card__tab--blue"><sup>$</sup>199</div>
    <h2 class="card__title"><span class="hl">ADVANCED</span> FOUNDATION REVIEW</h2>
    <p class="body card__text" style="top:32px">An advanced foundation review by a licensed foundation contractor is essential when buying a home, as it provides a detailed assessment beyond what a general home inspector can offer. While home inspectors are trained generalists who identify visible issues, a foundation contractor is a specialist with the expertise to evaluate structural integrity, detect hidden problems, and determine the severity of any concerns. This specialized review can uncover issues like uneven settling, cracks, or drainage problems that may require repairs, ensuring you have a clear understanding of the foundation's condition before making a significant investment.</p>
    <div class="card__img" role="img" aria-label="Cracked concrete foundation wall" style="top:37px;background:radial-gradient(ellipse at 45% 45%,#b9b4a6,#5b5850 80%)"></div>
  </article>

  <footer class="footer">
    <svg class="bg" width="535" height="54" viewBox="0 0 535 54" aria-hidden="true">
      <polygon points="0,0 150,0 186,49 0,49" fill="#0a5aa8"/>
      <polygon points="157,0 163,0 199,46 193,46" fill="#e21d27"/>
      <rect x="186" y="45" width="349" height="3" fill="#e21d27"/>
      <rect x="0" y="49" width="535" height="5" fill="#0a5aa8"/>
    </svg>
    <div class="footer__phone"><svg width="9" height="9" viewBox="0 0 10 10"><path d="M2 .5 4 2.5 3 4c.6 1.3 1.7 2.4 3 3l1.5-1 2 2-1.5 1.5C4.5 9.5.5 5.5.5 2z" fill="#e21d27"/></svg>800-555-0142</div>
    <div class="footer__contacts">
      <span><svg width="10" height="7" viewBox="0 0 10 7"><rect width="10" height="7" fill="#e21d27"/><path d="M0 0 5 4 10 0" stroke="#fff" fill="none"/></svg>hello@summitcrestinspect.com</span>
      <span><svg width="9" height="9" viewBox="0 0 10 10"><circle cx="5" cy="5" r="4.3" stroke="#e21d27" fill="none"/><ellipse cx="5" cy="5" rx="2" ry="4.3" stroke="#e21d27" fill="none"/><path d="M.7 5h8.6" stroke="#e21d27"/></svg>www.summitcrestinspect.com</span>
    </div>
  </footer>
</section>

</body>
</html>
```